Business Card for Polygraph business in Africa

Business Card . Polygraph Examiner based in Tanzania, East Africa.
Business Card will be used to disseminate contact information to potential clients.
It should convey that I am a professional specifically in the polygraph field and perform my work with integrity.

I have attached the business card that I'm currently using, which I threw together myself initially. It's not professional enough.

Target Market(s)

Banks, Accounting Firms, Government Ministries, Gas, Oil, & Gemstone Mining Concerns, Wildlife Conservation NGOs, International companies located in East Africa.

Industry/Entity Type

Business

Contact Information for Business Card

Veritrace Kilanga
Miriam Ostbrook
PO Box 48731
Arusha, Tanzania
+255 684 219 537
miriamostbrook@mailvera.example

Colors
00a990
f37122
faa54b

Requirements
Must have
• - Veritrace Kilanga (with the word "Polygraph" being more prominent than the word "Tanzania")
• - Forensic Examinations
• - Employment Screening
• - Should contain a logo of the Continental Truthtrace Society (of which I'm a member)
• - I would like an accent design (such as the polygraph "squiggles" of a cardio tracing or such as that)
• - My contact information (less prominent, but large enough to read legibly). I would also consider putting the contact information on the second side of the card.
Nice to have
• My color suggestions are changeable.
Should not have
• Anything "cutesy" or "cartoonish"

```html
<!DOCTYPE html>
<html lang="en">
<head>
<meta charset="utf-8">
<title>Veritrace Kilanga – Business Card</title>
<link href="https://fonts.googleapis.com/css2?family=Montserrat:wght@800&family=Lato:wght@400;700&display=swap" rel="stylesheet">
<style>
  :root {
    --backdrop: #2a2a2a;
    --orange: #f37122;
    --navy: #2b2f7f;
    --white: #ffffff;
    --ink: #2b2b33;
  }
  * { margin: 0; padding: 0; box-sizing: border-box; }
  html, body { width: 1200px; height: 852px; overflow: hidden; }
  body { background: var(--backdrop); position: relative; font-family: "Lato", sans-serif; }

  .card {
    position: absolute;
    width: 520px;
    height: 298px;
    border-radius: 18px;
    overflow: hidden;
  }

  /* Front: orange side */
  .card--front { left: 50px; top: 130px; background: var(--orange); color: var(--white); }
  .card--front .trace { position: absolute; left: 0; top: 0; width: 520px; height: 298px; }
  .card--front .brand-name {
    position: absolute; left: 228px; top: 112px;
    font-family: "Montserrat", sans-serif; font-weight: 800;
    font-size: 30px; line-height: 1.05; letter-spacing: 0.5px;
    color: var(--white); text-transform: uppercase;
  }
  .card--front .address {
    position: absolute; left: 0; right: 0; top: 236px;
    text-align: center; font-size: 12px; letter-spacing: 0.3px;
  }

  /* Back: white side */
  .card--back { left: 630px; top: 424px; background: var(--white); color: var(--ink); }
  .card--back .trace { position: absolute; left: 0; top: 0; width: 520px; height: 298px; }
  .card--back .footer-band { position: absolute; left: 0; right: 0; bottom: 0; height: 14px; background: var(--orange); }
  .membership-seal {
    position: absolute; left: 30px; top: 60px; width: 132px; height: 132px;
  }
  .card--back .brand-name {
    position: absolute; left: 262px; top: 54px;
    font-family: "Montserrat", sans-serif; font-weight: 800;
    font-size: 25px; line-height: 1.05; color: var(--navy); text-transform: uppercase;
  }
  .services { position: absolute; left: 268px; top: 118px; list-style: none; font-size: 14.5px; color: var(--ink); }
  .services li { display: flex; align-items: center; gap: 8px; margin-bottom: 3px; }
  .services li::before { content: ""; width: 6px; height: 6px; border-radius: 50%; background: var(--orange); }
  .contact-email {
    position: absolute; left: 196px; top: 176px;
    display: flex; align-items: center; gap: 6px; font-size: 13.5px;
  }
  .holder-name {
    position: absolute; left: 34px; top: 222px;
    font-family: "Montserrat", sans-serif; font-weight: 800;
    font-size: 17px; color: var(--navy); text-transform: uppercase;
  }
  .contact-phone {
    position: absolute; left: 34px; top: 248px;
    display: flex; align-items: center; gap: 6px; font-size: 14px;
  }
  .icon { width: 16px; height: 16px; flex: none; }
</style>
</head>
<body>

  <section class="card card--front" aria-label="Card front">
    <svg class="trace" viewBox="0 0 520 298" aria-hidden="true">
      <line x1="0" y1="188" x2="222" y2="148" stroke="#ffffff" stroke-width="2"/>
      <line x1="300" y1="104" x2="520" y2="64" stroke="#ffffff" stroke-width="2"/>
    </svg>
    <div class="brand-name">Veritrace<br>Kilanga</div>
    <p class="address">PO Box 48731, Arusha, Tanzania</p>
  </section>

  <section class="card card--back" aria-label="Card back">
    <svg class="trace" viewBox="0 0 520 298" aria-hidden="true">
      <line x1="0" y1="172" x2="30" y2="166" stroke="#2b2f7f" stroke-width="2"/>
      <line x1="162" y1="140" x2="255" y2="124" stroke="#2b2f7f" stroke-width="2"/>
      <line x1="470" y1="40" x2="520" y2="30" stroke="#2b2f7f" stroke-width="2"/>
    </svg>

    <svg class="membership-seal" viewBox="0 0 132 132" role="img" aria-label="Continental Truthtrace Society membership seal">
      <circle cx="66" cy="66" r="64" fill="#2b2f7f"/>
      <circle cx="66" cy="66" r="56" fill="#ffffff"/>
      <circle cx="66" cy="66" r="38" fill="#dfe0ef"/>
    </svg>

    <div class="brand-name">Veritrace<br>Kilanga</div>
    <ul class="services">
      <li>Forensic Examinations</li>
      <li>Employment Screening</li>
    </ul>

    <p class="contact-email">
      <svg class="icon" viewBox="0 0 16 16" aria-hidden="true">
        <circle cx="8" cy="8" r="8" fill="#f37122"/>
        <rect x="4" y="5" width="8" height="6" fill="none" stroke="#fff" stroke-width="1.2"/>
        <polyline points="4,5 8,8.5 12,5" fill="none" stroke="#fff" stroke-width="1.2"/>
      </svg>
      miriamostbrook@mailvera.example
    </p>

    <p class="holder-name">Miriam Ostbrook</p>
    <p class="contact-phone">
      <svg class="icon" viewBox="0 0 16 16" aria-hidden="true">
        <circle cx="8" cy="8" r="8" fill="#f37122"/>
        <path d="M5.2 4.2 L6.6 4 L7.2 6 L6.3 6.7 Q7 8.6 9.2 9.6 L9.9 8.7 L11.9 9.3 L11.7 10.8 Q8.6 11.6 6 9 Q4.3 7 5.2 4.2 Z" fill="#fff"/>
      </svg>
      +255 684 219 537
    </p>

    <div class="footer-band"></div>
  </section>

</body>
</html>
```